Cosmetic retail chain developes private label products. We need package designe for creme soap.

We need package designe for bar creme soap in cardboard package. Benchmark is Plim. The name of our private label for this product is Tirsa.

```html
<!DOCTYPE html>
<html lang="en">
<head>
<meta charset="utf-8">
<title>Tirsa white – beauty bar package</title>
<link rel="stylesheet" href="https://fonts.googleapis.com/css2?family=Quicksand:wght@400;500&family=Oswald:wght@500&display=swap">
<style>
  :root {
    --navy: #0f1a3e;
    --aqua-light: #d9eef2;
    --aqua-mid: #b3dbe2;
    --aqua-deep: #8fc6d1;
    --band: #ffffff;
    --gold: #c9b27a;
    --white: #ffffff;
  }
  html, body {
    margin: 0;
    padding: 0;
    overflow: hidden;
    background: var(--white);
  }
  .package-front {
    position: relative;
    width: 1200px;
    height: 857px;
    overflow: hidden;
    font-family: "Quicksand", sans-serif;
    color: var(--navy);
  }
  .watercolour-field {
    position: absolute;
    inset: 0;
    background:
      radial-gradient(ellipse 60% 45% at 15% 10%, rgba(255,255,255,0.7), transparent 70%),
      radial-gradient(ellipse 55% 50% at 75% 75%, var(--aqua-deep), transparent 75%),
      radial-gradient(ellipse 50% 40% at 35% 80%, rgba(255,255,255,0.45), transparent 70%),
      linear-gradient(160deg, var(--aqua-light) 0%, var(--aqua-mid) 55%, var(--aqua-deep) 100%);
  }
  .wave-band {
    position: absolute;
    inset: 0;
    width: 1200px;
    height: 857px;
  }
  .new-flag {
    position: absolute;
    left: 985px;
    top: 0;
    width: 121px;
    height: 120px;
    background: var(--navy);
    color: var(--white);
    box-sizing: border-box;
  }
  .new-flag::before {
    content: "";
    position: absolute;
    left: 13px;
    right: 13px;
    top: 27px;
    border-top: 1px solid var(--white);
  }
  .new-flag span {
    position: absolute;
    left: 0;
    right: 0;
    top: 38px;
    text-align: center;
    font-size: 34px;
    font-weight: 500;
    letter-spacing: 1px;
  }
  .brand-name {
    position: absolute;
    left: 135px;
    top: 120px;
    margin: 0;
    font-size: 138px;
    font-weight: 400;
    line-height: 1;
    letter-spacing: 1px;
  }
  .brand-rule {
    position: absolute;
    left: 147px;
    top: 286px;
    width: 358px;
    border-top: 1px solid var(--navy);
  }
  .variant {
    position: absolute;
    left: 404px;
    top: 290px;
    font-size: 33px;
    font-weight: 500;
  }
  .claim-seal {
    position: absolute;
    left: 204px;
    top: 559px;
    width: 172px;
    height: 172px;
    border: 1.5px solid var(--navy);
    border-radius: 50%;
    background: var(--white);
    box-sizing: border-box;
    display: flex;
    align-items: center;
    justify-content: center;
    text-align: center;
    font-size: 24px;
    line-height: 1.3;
    font-weight: 500;
    padding-bottom: 6px;
  }
  .cream-seal {
    position: absolute;
    left: 250px;
    top: 699px;
    width: 126px;
    height: 126px;
    border: 1.5px solid var(--gold);
    border-radius: 50%;
    background: var(--white);
    box-sizing: border-box;
    display: flex;
    align-items: center;
    justify-content: center;
    text-align: center;
    color: var(--gold);
    font-size: 18px;
    line-height: 1.25;
  }
  .net-weight {
    position: absolute;
    left: 617px;
    top: 774px;
    font-family: "Oswald", sans-serif;
    font-weight: 500;
    font-size: 12px;
    letter-spacing: -0.2px;
    color: var(--navy);
  }
</style>
</head>
<body>
  <main class="package-front">
    <div class="watercolour-field" role="img" aria-label="Soft pale aqua watercolour wash background"></div>

    <svg class="wave-band" viewBox="0 0 1200 857" role="img" aria-label="White wave band with a faint damask pattern">
      <path d="M0 190 C 150 160, 300 140, 470 150 C 650 160, 800 220, 960 215 C 1060 212, 1140 185, 1200 170 L 1200 392 C 1100 400, 1000 420, 900 410 C 750 395, 650 355, 500 345 C 330 335, 150 380, 0 420 Z" fill="var(--band)"/>
    </svg>

    <div class="new-flag"><span>NEW</span></div>

    <h1 class="brand-name">Tirsa</h1>
    <div class="brand-rule"></div>
    <div class="variant">white</div>

    <div class="claim-seal">beauty bar<br>with deep<br>moisture</div>
    <div class="cream-seal">moisturising<br>cream</div>

    <div class="net-weight">NET WT 4 OZ/113g</div>
  </main>
</body>
</html>
```